Business Card Design Project

We require business cards to be produced with the following design
http://files.pixelvault-demo.net/img/50329/84172/84172_2093548_50329_image.jpg
Rather than bright meadow, please use Vantelo as the comapny name.
Please also use the following contact details:
1.
Daniel Overbeck
Entrepreneur
07423158871
doverbeck@vantelo-demo.com
2.
Tom Ashworth
Founder
07539402217
tashworth@vantelo-demo.com
Please add:
Facebook favicion facebook.com/vantelo
Linked in favicon linkedin/danieloverbeck
Skype favicon doverbeck
Linked in favicon linkedin/thomasashworth
Skype favicon thomasashworth
Google Plus favicon tomashworth@mailbox-demo.net
To the back

```html
<!DOCTYPE html>
<html lang="en">
<head>
<meta charset="utf-8">
<title>Vantelo – Business Card</title>
<link rel="stylesheet" href="https://fonts.googleapis.com/css2?family=Arimo&family=PT+Sans&display=swap">
<style>
  :root {
    --card-white: #ffffff;
    --brand-red: #dc0000;
    --mark-red: #e3050f;
    --heading-grey: #a9a9a9;
    --ink: #111111;
  }
  html, body {
    margin: 0;
    padding: 0;
    width: 1200px;
    height: 686px;
    overflow: hidden;
    background: var(--card-white);
  }
  .card {
    position: relative;
    width: 1200px;
    height: 686px;
    background: var(--card-white);
    overflow: hidden;
  }
  .company-line {
    position: absolute;
    left: 40px;
    top: 84px;
    margin: 0;
    font-family: "Arimo", Arial, sans-serif;
    font-weight: 400;
    font-size: 87px;
    line-height: 1;
    letter-spacing: 0.5px;
    color: var(--heading-grey);
    white-space: nowrap;
  }
  .brand-square {
    position: absolute;
    left: 978px;
    top: 18px;
    width: 190px;
    height: 190px;
    background: var(--mark-red);
  }
  .identity {
    position: absolute;
    left: 621px;
    top: 304px;
    font-family: "PT Sans", Tahoma, sans-serif;
    color: var(--ink);
  }
  .identity .role {
    margin: 0;
    font-size: 35px;
    line-height: 1;
  }
  .identity .name {
    margin: 18px 0 0;
    font-size: 70px;
    font-weight: 400;
    line-height: 1;
    letter-spacing: 0.5px;
  }
  .contact-band {
    position: absolute;
    left: 0;
    top: 451px;
    width: 1200px;
    height: 235px;
    background: var(--brand-red);
  }
  .band-square {
    position: absolute;
    left: -24px;
    top: 100px;
    width: 160px;
    height: 160px;
    background: var(--card-white);
  }
  .contact-details {
    position: absolute;
    right: 51px;
    top: 94px;
    margin: 0;
    font-family: "PT Sans", Tahoma, sans-serif;
    font-style: normal;
    font-size: 35px;
    line-height: 46px;
    text-align: right;
    color: var(--ink);
  }
  .contact-details span { display: block; }
</style>
</head>
<body>
  <main class="card">
    <h1 class="company-line">A VANTELO COMPANY</h1>
    <div class="brand-square"></div>

    <section class="identity">
      <p class="role">Entrepreneur</p>
      <h2 class="name">Daniel Overbeck</h2>
    </section>

    <section class="contact-band">
      <div class="band-square"></div>
      <address class="contact-details">
        <span class="phone">074 23 15 88 71</span>
        <span class="email">doverbeck@vantelo-demo.com</span>
      </address>
    </section>
  </main>
</body>
</html>
```